Coastal Bright Sweep Business Card

We are a cleaning and waste management company with the slogan "making waste to landfill a thing of the past". We would like a re-design of our current business card. On the front we want to continue to use our logo as the focus point. On the back, we want the whole thing re-done to be less busy. We want the staff member’s name, the job title, mobile number, email and website. We do not want the address on the card. We still want the green, black and blue colours used, but a new font for the information on the back. Please do not change the logo design at all. We are also thinking about using icons to replace the text ‘mobile, email, website’. The “events + commercial” banner needs to be incorporated somewhere and needs to read “events + commercial + waste”. Another important point for consideration is that we are very concerned about being environmentally sustainable and will be printing on recycled paper. All designs should be made to compliment this in regards to boldness and colouring. Please find attached our logo, our colour chart and an image of our current business card.

```html
<!DOCTYPE html>
<html lang="en">
<head>
<meta charset="utf-8">
<title>Coastal Bright Sweep – Business Card</title>
<link rel="stylesheet" href="https://fonts.googleapis.com/css2?family=Montserrat:wght@600;700;800&display=swap">
<style>
  :root {
    --stage: #2e2e2e;
    --paper: #ece5d4;
    --navy: #173f6e;
    --green: #6cb33f;
    --blue: #1ea0dc;
    --white: #ffffff;
    --card-w: 680px;
    --card-h: 389px;
  }
  * { box-sizing: border-box; margin: 0; padding: 0; }
  html, body {
    width: 1200px; height: 900px; overflow: hidden;
    background: var(--stage);
    font-family: "Montserrat", Arial, sans-serif;
  }
  .stage {
    position: relative; width: 1200px; height: 900px;
    display: flex; flex-direction: column; align-items: center;
    justify-content: center; gap: 40px;
  }
  .card {
    position: relative; width: var(--card-w); height: var(--card-h);
    background: var(--paper); overflow: hidden;
    box-shadow: 0 6px 18px rgba(0,0,0,0.45);
  }
  .brand-name {
    color: var(--navy); font-weight: 800; line-height: 1.02;
    letter-spacing: 0.01em;
  }

  /* Front */
  .card-front .brand {
    position: absolute; left: 0; right: 0; top: 78px;
    display: flex; flex-direction: column; align-items: center;
  }
  .card-front .brand-name { font-size: 58px; text-align: left; }
  .card-front .tagline {
    position: absolute; left: 0; right: 0; bottom: 62px;
    text-align: center; color: var(--navy);
    font-weight: 700; font-size: 17px; letter-spacing: 0.01em;
  }

  /* Back */
  .card-back .brand {
    position: absolute; right: 34px; top: 36px;
  }
  .card-back .brand-name { font-size: 34px; }
  .person { position: absolute; left: 44px; top: 112px; }
  .person-name { color: var(--navy); font-weight: 800; font-size: 22px; letter-spacing: 0.01em; }
  .person-role { color: var(--green); font-weight: 800; font-size: 17px; margin-top: 4px; letter-spacing: 0.02em; }
  .contacts { position: absolute; left: 44px; top: 222px; list-style: none; }
  .contact {
    display: flex; align-items: center; gap: 8px;
    color: var(--navy); font-weight: 700; font-size: 17px; line-height: 26px;
  }
  .contact svg { width: 18px; height: 18px; flex: none; }
  .service-band {
    position: absolute; left: 0; bottom: 34px; width: 610px; height: 40px;
    background: var(--blue); color: var(--white);
    display: flex; align-items: center; padding-left: 40px;
    font-weight: 700; font-size: 19px; letter-spacing: 0.32em;
  }
  .band-fold { position: absolute; left: 586px; bottom: 74px; width: 24px; height: 24px; }
</style>
</head>
<body>
<main class="stage">

  <section class="card card-front" aria-label="Card front">
    <div class="brand">
      <p class="brand-name">Coastal<br>Bright<br>Sweep</p>
    </div>
    <p class="tagline">making waste to landfill a thing of the past</p>
  </section>

  <section class="card card-back" aria-label="Card back">
    <div class="brand">
      <p class="brand-name">Coastal<br>Bright<br>Sweep</p>
    </div>

    <div class="person">
      <p class="person-name">MORGAN ELLERY</p>
      <p class="person-role">CLIENT MANAGER</p>
    </div>

    <ul class="contacts">
      <li class="contact">
        <svg viewBox="0 0 18 18" aria-hidden="true"><rect x="1" y="1" width="16" height="16" rx="4" fill="none" stroke="var(--blue)" stroke-width="1.6"/><rect x="6" y="4" width="6" height="10" rx="1.2" fill="none" stroke="var(--navy)" stroke-width="1.4"/><circle cx="9" cy="12" r="0.8" fill="var(--navy)"/></svg>
        <span>0400 555 218</span>
      </li>
      <li class="contact">
        <svg viewBox="0 0 18 18" aria-hidden="true"><rect x="1" y="1" width="16" height="16" rx="4" fill="none" stroke="var(--blue)" stroke-width="1.6"/><rect x="4" y="5.5" width="10" height="7" rx="1" fill="none" stroke="var(--navy)" stroke-width="1.4"/><path d="M4.5 6l4.5 3.5L13.5 6" fill="none" stroke="var(--navy)" stroke-width="1.4"/></svg>
        <span>mellery@coastalbrightsweep.com.au</span>
      </li>
      <li class="contact">
        <svg viewBox="0 0 18 18" aria-hidden="true"><rect x="1" y="1" width="16" height="16" rx="4" fill="none" stroke="var(--blue)" stroke-width="1.6"/><circle cx="9" cy="9" r="4.6" fill="none" stroke="var(--navy)" stroke-width="1.3"/><path d="M4.4 9h9.2M9 4.4c-2 2.6-2 6.6 0 9.2M9 4.4c2 2.6 2 6.6 0 9.2" fill="none" stroke="var(--navy)" stroke-width="1.1"/></svg>
        <span>www.coastalbrightsweep.com.au</span>
      </li>
    </ul>

    <svg class="band-fold" viewBox="0 0 24 24" aria-hidden="true">
      <polygon points="24,0 24,24 0,24" fill="var(--navy)"/>
      <polygon points="24,0 24,12 12,12" fill="var(--green)"/>
    </svg>
    <p class="service-band">EVENTS + COMMERCIAL + WASTE</p>
  </section>

</main>
</body>
</html>
```